Looking for a PowerPoint design for a Pharmaceutical Company

We need a PowerPoint template design to be used company-wide. We are a pharmaceutical company with 63 years of history and want to use a new template design to work more efficiently and effectively. Below are some of the things we are looking for in the new template design.

- Simple, modern, and professional

- Practical for every day use (easy to read, easy to create)

- Slides will be mainly projected or viewed on screens, but should also work fine when printed. (e.g. We do not want to use up our inks / toners printing several pages..)

- It would be great if you could provide us a list of colors that can be effectively used in the slides. (e.g. for highlighting fonts / multiple graph colors / etc.)

- Just as an FYI, our current logo image is (dark) blue. I am not uploading the logo image here because we do not want you to be limited by the current logo image. Depending on the design, we may / may not put our logo image on the slides.

Please feel free to reach out to me if you have any questions. I look forward to seeing your design. Thank you!

Target Market(s)

Pharmaceutical industry. (To be used internally and externally)

Industry/Entity Type

Pharmaceutical

Font styles to use
Sans Serif

Requirements
Must have
• Title slide, Subtitle slide, graphs, charts, tables, bullet points, and any other slide style components normally included.
Nice to have
• - As we are in the pharma industry, we want the slides to give credibility. But we do not want it look "old", "boring", or "typical". Feel free to use unique / fresh colors.
Should not have
• - TOO many colors
• - Please do not use the images on our website, which contain faces. (Any image with faces in it...) They are stock images we bought for the website, and we do not want the images on our slides. (e.g. image of running woman on the main page, image of a surgeon, image of kids playing soccer, etc.)
• - We are not looking for a design that is a modified version of our website design. We are looking for something new.

```html
<!DOCTYPE html>
<html lang="en">
<head>
<meta charset="utf-8">
<title>Veltra Pharm – Presentation Template</title>
<link href="https://fonts.googleapis.com/css2?family=Open+Sans:ital,wght@0,300;0,400;0,600;1,300;1,400&display=swap" rel="stylesheet">
<style>
:root{
  --bg:#d9d9d9;
  --white:#ffffff;
  --cyan:#6fe0e8;
  --cyan-deep:#2cc6d2;
  --sky:#3aa6df;
  --slate:#6787bb;
  --navy:#3e5d8f;
  --grey:#6b7180;
  --grey-light:#f3f3f3;
  --grey-mid:#c9cbd0;
  --ink:#4a4a4a;
  --ink-soft:#9a9a9a;
}
*{margin:0;padding:0;box-sizing:border-box}
html,body{width:1200px;height:1000px;overflow:hidden}
body{background:var(--bg);font-family:"Open Sans",Arial,sans-serif;color:var(--ink);position:relative}
.slide{position:absolute;width:367px;height:207px;background:var(--white);overflow:hidden}
.abs{position:absolute}
.photo{position:absolute}
.brand{position:absolute;display:flex;align-items:center;gap:5px;color:var(--white);font-size:12px;font-weight:400;white-space:nowrap}
.brand .dot{width:16px;height:16px;border-radius:50%;background:var(--navy);flex:none}
.brand.dark{color:var(--navy)}
.head-bar{position:absolute;left:0;top:0;width:10px;height:40px;background:var(--cyan)}
.head-title{position:absolute;left:21px;top:9px;font-size:13px;font-weight:400;color:var(--ink);letter-spacing:-.2px}
.head-sub{position:absolute;left:21px;top:27px;font-size:9.5px;color:var(--ink-soft)}
.num{position:absolute;right:1px;top:0;width:22px;height:22px;background:var(--sky);color:var(--white);font-size:13px;display:flex;align-items:center;justify-content:center}
.tiny{font-size:5.6px;line-height:1.45;color:var(--ink-soft)}
.body-it{font-style:italic;font-weight:300;font-size:6.2px;line-height:1.45;color:var(--ink);text-align:justify}

/* title slide */
.title-main{right:16px;top:103px;text-align:right;color:var(--white);font-style:italic;font-weight:300;font-size:19px;line-height:1.15}
.title-note{right:16px;top:160px;width:165px;text-align:right;color:var(--white);font-size:5.4px;line-height:1.5}

/* agenda */
.agenda-panel{left:0;top:0;width:185px;height:207px;background:var(--slate)}
.agenda-box{left:73px;top:37px;width:294px;height:48px;background:var(--grey)}
.agenda-word{left:88px;top:50px;color:var(--white);font-style:italic;font-weight:300;font-size:22px;letter-spacing:.5px}
.agenda-note{left:194px;top:40px;width:166px;color:#e6e6e6;font-size:5.3px;line-height:1.45;text-align:justify}
.item{position:absolute;display:flex;align-items:flex-start;gap:4px;width:170px}
.item .n{width:22px;height:17px;background:var(--navy);color:var(--white);font-style:italic;font-size:12px;display:flex;align-items:center;justify-content:center;border-right:2px solid var(--cyan)}
.item .t{font-style:italic;font-size:5.6px;color:var(--cyan);margin-top:1px}
.item .d{font-size:4.6px;color:#eef2f8}
.item.light .d{color:var(--ink-soft)}

/* mission */
.mission-photo{left:0;top:58px;width:367px;height:102px;background:linear-gradient(90deg,#4d79a8,#6f9cc6 45%,#8fb6d6)}
.mission-text{right:18px;top:90px;width:314px;text-align:right;color:var(--white);font-style:italic;font-weight:300;font-size:12.6px;line-height:1.3}
.mission-band{left:0;top:160px;width:367px;height:17px;background:var(--cyan)}

/* about */
.about-lead{right:12px;top:17px;width:164px;text-align:right;color:var(--cyan-deep);font-weight:300;font-size:10.3px;line-height:1.25}
.big63{left:74px;top:34px;font-size:98px;font-weight:300;color:var(--slate);letter-spacing:-5px;line-height:1}
.years-box{left:10px;top:127px;width:178px;height:80px;background:var(--slate)}
.years{left:10px;top:136px;width:172px;text-align:right;color:var(--cyan);font-style:italic;font-size:11px}
.about-grey{left:188px;top:82px;width:179px;height:125px;background:var(--grey-light)}
.about-text{left:198px;top:112px;width:162px;text-align:right;font-style:italic;font-size:6.1px;line-height:1.4;color:var(--slate)}

/* section break */
.section-photo{left:0;top:0;width:367px;height:207px;background:radial-gradient(circle at 78% 52%,#8fd0ee 0,#4cb1e4 35%,#3aa6df 70%)}
.section-strip{left:0;top:0;width:10px;height:58px;background:#9ab0c8}
.section-text{left:22px;top:14px;color:var(--white);font-style:italic;font-weight:300;font-size:6.2px;line-height:1.45}
.section-title{right:14px;top:166px;color:var(--white);font-style:italic;font-weight:300;font-size:18px}

/* presentation */
.icon-box{left:27px;top:62px;width:108px;height:108px;background:var(--grey);display:flex;align-items:center;justify-content:center}
.pres-text{left:154px;top:66px;width:194px}

/* core values */
.value{position:absolute;width:102px;height:101px;display:flex;flex-direction:column;align-items:center;justify-content:center;gap:6px;color:var(--white);font-size:8px}
.values-text{left:18px;top:122px;width:122px;text-align:right}

/* text slide */
.text-right{left:190px;top:0;width:177px;height:207px;background:#f5f5f5}
.col{position:absolute;width:160px;border-left:2px solid #d4d4d4;padding-left:7px}
.col h3{font-style:italic;font-weight:300;font-size:12.5px;line-height:1.3;color:var(--sky);margin-bottom:18px}

/* pharma business */
.tile{position:absolute;width:80px;height:80px;display:flex;align-items:center;justify-content:center}
.tile-text{position:absolute;width:80px;text-align:center;font-weight:400;font-size:6.3px;line-height:1.4;color:var(--ink)}
</style>
</head>
<body>

<!-- 1 Title -->
<section class="slide" style="left:24px;top:160px">
  <div class="photo" role="img" aria-label="Photo of the company headquarters building, tinted blue to cyan" style="inset:0;background:linear-gradient(120deg,#4a9fd8 0%,#55b8e2 45%,#72dfe8 100%)"></div>
  <div class="brand" style="right:16px;top:62px;font-size:15px;gap:6px"><span class="dot" style="width:22px;height:22px"></span>Veltra Pharm</div>
  <h1 class="abs title-main">Building a Healthier<br>Future Together</h1>
  <p class="abs title-note">We aspire to improve health and well-being of people around the world by providing innovative products and solutions, so that people can enjoy healthier and better lives.</p>
</section>

<!-- 2 Agenda -->
<section class="slide" style="left:416px;top:160px">
  <div class="abs agenda-panel"></div>
  <div class="brand dark" style="right:10px;top:10px"><span class="dot"></span>Veltra Pharm</div>
  <div class="abs agenda-box"></div>
  <h2 class="abs agenda-word">AGENDA</h2>
  <p class="abs agenda-note">Our agenda covers the key topics of today, from recent results and ongoing research to the plans and goals we share for the coming year ahead. Each section below opens with a short summary and closes with the next steps agreed by our teams across every business unit.</p>
  <div class="item" style="left:15px;top:99px"><span class="n">01</span><div><div class="t">Title of the Section</div><div class="d">Short description of this section goes here</div></div></div>
  <div class="item" style="left:15px;top:136px"><span class="n">02</span><div><div class="t">Title of the Section</div><div class="d">Short description of this section goes here</div></div></div>
  <div class="item" style="left:15px;top:172px"><span class="n">03</span><div><div class="t">Title of the Section</div><div class="d">Short description of this section goes here</div></div></div>
  <div class="item light" style="left:194px;top:99px"><span class="n">04</span><div><div class="t">Title of the Section</div><div class="d">Short description of this section goes here</div></div></div>
  <div class="item light" style="left:194px;top:136px"><span class="n">05</span><div><div class="t">Title of the Section</div><div class="d">Short description of this section goes here</div></div></div>
  <div class="item light" style="left:194px;top:172px"><span class="n">06</span><div><div class="t">Title of the Section</div><div class="d">Short description of this section goes here</div></div></div>
</section>

<!-- 3 Mission -->
<section class="slide" style="left:809px;top:160px">
  <div class="head-bar"></div>
  <h2 class="head-title">MISSION</h2>
  <p class="head-sub">Subtitle Goes Here</p>
  <div class="num">3</div>
  <div class="photo mission-photo" role="img" aria-label="Photo of laboratory test tubes in soft blue tones"></div>
  <p class="abs mission-text">Our mission is not just to provide cure for patients suffering from illness, but also to provide better lives to everyone so that people can enjoy healthier and happier lives.</p>
  <div class="abs mission-band"></div>
  <div class="brand" style="right:10px;top:161px;font-size:10px"><span class="dot" style="width:13px;height:13px"></span>Veltra Pharm</div>
</section>

<!-- 4 About -->
<section class="slide" style="left:24px;top:396px">
  <div class="head-bar" style="height:60px"></div>
  <h2 class="head-title">ABOUT US</h2>
  <p class="head-sub">Subtitle Goes Here</p>
  <p class="abs about-lead">Veltra Pharm is committed to its mission to improve the health and well-being of people around the world.</p>
  <div class="abs years-box"></div>
  <div class="abs big63">63</div>
  <p class="abs years">YEARS OF HISTORY</p>
  <div class="abs about-grey"></div>
  <p class="abs about-text">Since 1953, we have strived to not only treat the sick but also to help everyone live healthier and happier lives through our various businesses, including pharmaceutical, medical device, and consumer health businesses. While providing highest quality products through continuous technical innovations and investments in the manufacturing facilities, Veltra Pharm always seeks to create new values through R&amp;D and open innovation.</p>
</section>

<!-- 5 Section break -->
<section class="slide" style="left:416px;top:396px">
  <div class="photo section-photo" role="img" aria-label="Photo of a pipette dropping liquid into a petri dish, in bright blue"></div>
  <div class="abs section-strip"></div>
  <p class="abs section-text">omnis voluptas assumenda est,<br>omnis dolor repellendus.<br>Temporibus autem quibusdam et<br>aut officiis debitis aut rerum<br>necessitatibus saepe eveniet.</p>
  <div class="brand" style="right:14px;top:144px;font-size:13px"><span class="dot" style="width:18px;height:18px"></span>Veltra Pharm</div>
  <h2 class="abs section-title">Section Break</h2>
</section>

<!-- 6 Presentation -->
<section class="slide" style="left:809px;top:396px">
  <div class="head-bar"></div>
  <h2 class="head-title">PRESENTATION</h2>
  <p class="head-sub">Subtitle Goes Here</p>
  <div class="num">6</div>
  <div class="abs icon-box">
    <svg width="72" height="72" viewBox="0 0 72 72" fill="none" stroke="#6fe0e8" stroke-width="2.4" stroke-linecap="round">
      <g transform="rotate(-45 30 32)"><rect x="8" y="22" width="44" height="20" rx="10"/><line x1="30" y1="22" x2="30" y2="42"/><circle cx="20" cy="29" r="1"/><circle cx="16" cy="35" r="1"/><circle cx="22" cy="36" r="1"/></g>
      <circle cx="50" cy="50" r="13"/><line x1="41" y1="59" x2="59" y2="41"/>
    </svg>
  </div>
  <div class="abs pres-text">
    <p class="body-it">At vero eos et accusamus et iusto odio dignissimos ducimus qui blanditiis praesentium voluptatum deleniti atque corrupti quos dolores et quas molestias excepturi sint occaecati cupiditate non provident, similique sunt in culpa qui officia deserunt mollitia animi, id est laborum et dolorum fuga. Et harum quidem rerum facilis est et expedita distinctio.</p>
    <p class="body-it" style="margin-top:6px">omnis voluptas assumenda est, omnis dolor repellendus. Temporibus autem quibusdam et aut officiis debitis aut rerum necessitatibus saepe eveniet ut et voluptates repudiandae sint et molestiae non recusandae. Itaque earum rerum hic tenetur a sapiente delectus.</p>
  </div>
</section>

<!-- 7 Core values -->
<section class="slide" style="left:24px;top:632px">
  <div class="head-bar"></div>
  <h2 class="head-title">CORE VALUES</h2>
  <p class="head-sub">Subtitle Goes Here</p>
  <p class="abs body-it values-text" style="text-align:right">At vero eos et accusamus et iusto odio dignissimos ducimus qui blanditiis praesentium voluptatum deleniti atque corrupti quos dolores et quas molestias excepturi sint occaecati cupiditate non provident, similique sunt in culpa qui officia deserunt mollitia animi, id est laborum et dolorum fuga. Et harum quidem rerum facilis est et expedita distinctio.</p>
  <div class="value" style="left:160px;top:0;background:var(--navy)">
    <svg width="50" height="40" viewBox="0 0 50 40" fill="none" stroke="#6fe0e8" stroke-width="1.8" stroke-linejoin="round" stroke-linecap="round"><path d="M30 6c3-4 9-2 8 3-1 4-8 8-8 8s-7-4-8-8c-1-5 5-7 8-3z"/><path d="M4 26h10l8-4h10a3 3 0 010 6H22"/><path d="M14 34l8 0 20-10a3 3 0 00-3-5l-8 3"/></svg>
    <span>VALUE 1</span></div>
  <div class="value" style="left:266px;top:0;background:var(--grey)">
    <svg width="44" height="44" viewBox="0 0 44 44" fill="none" stroke="#6fe0e8" stroke-width="1.8"><circle cx="22" cy="22" r="5"/><circle cx="22" cy="5" r="3"/><circle cx="22" cy="39" r="3"/><circle cx="5" cy="22" r="3"/><circle cx="39" cy="22" r="3"/><circle cx="10" cy="10" r="3"/><circle cx="34" cy="10" r="3"/><circle cx="10" cy="34" r="3"/><circle cx="34" cy="34" r="3"/><path d="M22 8v9M22 27v9M8 22h9M27 22h9M12 12l6 6M32 12l-6 6M12 32l6-6M32 32l-6-6"/></svg>
    <span>VALUE 2</span></div>
  <div class="value" style="left:160px;top:106px;background:var(--cyan-deep)">
    <svg width="46" height="40" viewBox="0 0 46 40" fill="none" stroke="#ffffff" stroke-width="1.8" stroke-linecap="round"><path d="M4 8l14 14M42 8L28 22M4 32l14-10M42 32L28 22"/><circle cx="23" cy="22" r="6"/></svg>
    <span>VALUE 3</span></div>
  <div class="value" style="left:266px;top:106px;background:var(--sky)">
    <svg width="46" height="40" viewBox="0 0 46 40" fill="none" stroke="#ffffff" stroke-width="1.8" stroke-linecap="round"><rect x="22" y="6" width="18" height="14"/><path d="M8 38V26h14M4 38h38M30 20v18"/><circle cx="14" cy="14" r="4"/></svg>
    <span>VALUE 4</span></div>
</section>

<!-- 8 Text based -->
<section class="slide" style="left:416px;top:632px">
  <div class="abs text-right"></div>
  <div class="head-bar"></div>
  <h2 class="head-title">TEXT BASED SLIDE</h2>
  <p class="head-sub">Subtitle Goes Here</p>
  <div class="col" style="left:17px;top:70px">
    <h3>CMO<br>Business</h3>
    <p class="tiny">At vero eos et accusamus et iusto odio dignissimos ducimus qui blanditiis praesentium voluptatum deleniti atque corrupti quos dolores et quas molestias excepturi sint occaecati cupiditate non provident.</p>
  </div>
  <div class="col" style="left:190px;top:70px">
    <h3>Medical Device<br>Business</h3>
    <p class="tiny">At vero eos et accusamus et iusto odio dignissimos ducimus qui blanditiis praesentium voluptatum deleniti atque corrupti quos dolores et quas molestias excepturi sint occaecati cupiditate non provident.</p>
  </div>
</section>

<!-- 9 Pharmaceutical business -->
<section class="slide" style="left:809px;top:632px">
  <div class="head-bar" style="height:60px"></div>
  <h2 class="head-title">PHARMACEUTICAL BUSINESS</h2>
  <p class="head-sub">Subtitle Goes Here</p>
  <div class="num">9</div>
  <div class="tile" style="left:44px;top:58px;background:var(--slate)">
    <svg width="40" height="46" viewBox="0 0 40 46" fill="none" stroke="#ffffff" stroke-width="1.8" stroke-linecap="round"><rect x="14" y="4" width="8" height="18" transform="rotate(-25 18 13)"/><path d="M8 42h26M12 42v-4h18v4M22 24a10 10 0 01-4 14"/><circle cx="22" cy="24" r="3"/></svg>
  </div>
  <div class="tile" style="left:144px;top:58px;background:var(--cyan)">
    <svg width="40" height="46" viewBox="0 0 40 46" fill="none" stroke="#ffffff" stroke-width="1.8" stroke-linecap="round"><path d="M8 4h26M13 4v34a3 3 0 006 0V4M25 4v34a3 3 0 006 0V4M13 20h6M25 24h6M6 44h30"/></svg>
  </div>
  <div class="tile" style="left:244px;top:58px;background:var(--grey-mid)">
    <svg width="40" height="46" viewBox="0 0 40 46" fill="none" stroke="#ffffff" stroke-width="1.8" stroke-linejoin="round" stroke-linecap="round"><path d="M14 4h12M16 4v14L5 40h30L24 18V4M10 30h20"/><circle cx="18" cy="35" r="1.5"/><circle cx="24" cy="33" r="1"/></svg>
  </div>
  <p class="tile-text" style="left:44px;top:146px">At vero eos et accusamus et iusto odio dignissimos ducimus qui blanditiis praesentium voluptatum deleniti atque .</p>
  <p class="tile-text" style="left:144px;top:146px">At vero eos et accusamus et iusto odio dignissimos ducimus qui blanditiis praesentium voluptatum deleniti atque .</p>
  <p class="tile-text" style="left:244px;top:146px">At vero eos et accusamus et iusto odio dignissimos ducimus qui blanditiis praesentium voluptatum deleniti atque .</p>
</section>

</body>
</html>
```